ALL TEXT GRAPHICS TM May 2025 for Instagram

We are looking for a series of social media graphics for Instagram (new size: 4:5 (1080 x 1350 pixels) ratio that are ALL TEXT. We want the following quotes below on each graphic; one quote per graphic. AND, In very small letters at the bottom of each graphic, add @TovaMarshOnline
The look and feel of these graphics should be complimentary to the color palette attached below; but keep them simple. But the design is up to you; at the end of this document, I provided various samples of all text graphics that I like as examples.
Target Market(s)
women looking to lose weight
Look and feel

```html
<!DOCTYPE html>
<html lang="en">
<head>
<meta charset="utf-8">
<title>That stubborn weight?</title>
<link rel="stylesheet" href="https://fonts.googleapis.com/css2?family=Exo+2:wght@600;700;800&display=swap">
<style>
  :root {
    --ink: #ffffff;
    --night: #050303;
    --curtain: #4a1410;
    --curtain-deep: #2a0b08;
    --skin: #8a5a46;
    --frame: #6b4a36;
  }
  html, body {
    margin: 0;
    padding: 0;
    width: 960px;
    height: 1200px;
    overflow: hidden;
    background: var(--night);
  }
  .post {
    position: relative;
    width: 960px;
    height: 1200px;
    overflow: hidden;
    background: var(--night);
    font-family: "Exo 2", "Arial", sans-serif;
    color: var(--ink);
    text-align: center;
  }
  .post__photo {
    position: absolute;
    inset: 0;
    background:
      radial-gradient(ellipse 300px 420px at 250px 420px, rgba(138, 90, 70, 0.55), transparent 70%),
      radial-gradient(ellipse 260px 520px at 760px 380px, rgba(90, 60, 48, 0.45), transparent 75%),
      radial-gradient(ellipse 520px 560px at 420px 260px, var(--curtain), transparent 75%),
      linear-gradient(180deg, var(--curtain-deep) 0%, #1a0806 45%, var(--night) 80%);
  }
  .post__shade {
    position: absolute;
    inset: 0;
    background: linear-gradient(180deg, rgba(0,0,0,0) 30%, rgba(0,0,0,0.55) 55%, rgba(0,0,0,0.95) 78%);
  }
  .post__copy {
    position: absolute;
    left: 0;
    right: 0;
    top: 440px;
  }
  .headline {
    margin: 0;
    font-weight: 800;
    line-height: 1;
  }
  .headline__lead {
    display: block;
    font-size: 72px;
    letter-spacing: -0.5px;
  }
  .headline__key {
    display: block;
    font-size: 136px;
    letter-spacing: -2px;
    margin-top: -8px;
  }
  .reassure {
    margin: 40px 0 0;
    font-weight: 600;
    font-size: 39px;
    line-height: 1.14;
  }
  .promise {
    margin: 42px 0 0;
    font-weight: 800;
    font-size: 56px;
    line-height: 1;
  }
  .promise__emoji {
    display: block;
    margin-top: 14px;
    font-size: 50px;
    line-height: 1;
  }
  .handle {
    position: absolute;
    left: 0;
    right: 0;
    top: 1076px;
    margin: 0;
    font-weight: 700;
    font-size: 15px;
  }
</style>
</head>
<body>
  <main class="post">
    <div class="post__photo" role="img" aria-label="Photo of a woman in a sports bra looking at her reflection in a mirror, warm red curtain behind, fading to black"></div>
    <div class="post__shade"></div>
    <section class="post__copy">
      <h1 class="headline">
        <span class="headline__lead">That stubborn</span>
        <span class="headline__key">weight?</span>
      </h1>
      <p class="reassure">It’s not your fault.<br>Your hormones are to blame and<br>you’re not alone;</p>
      <p class="promise">But there is a fix.<span class="promise__emoji">😍</span></p>
    </section>
    <p class="handle">and@TovaMarshOnline</p>
  </main>
</body>
</html>
```